Business Cards- The Estate at Brookhollow Golf Club

We would like our business cards to look more high-end. We are a wedding venue that has been in business for 60+ years. We like our logo and our colors - primarily green and a touch of gold/beige. The owner wants our business cards to look more special..

Target Market(s)

Brides who have already toured our venue

Industry/Entity Type

Wedding venue - mansion

Contact Information for Business Card

Name, email, physical address, phone number

Colors
00AB8E
00BBA5
67D7C9
C6EFE9
E9F9F6

Requirements
Must have
• I think we would like our cards to be so pretty that people will want to keep them and will remember the venue. The venue is historic (built in 1850) and beautiful.
Nice to have
• Could we put an image of the building on one side and the contact info on the other?
Should not have
• The color black

```html
<!DOCTYPE html>
<html lang="en">
<head>
<meta charset="utf-8">
<title>The Estate at Brookhollow Golf Club — Business Cards</title>
<link rel="stylesheet" href="https://fonts.googleapis.com/css2?family=Arimo:wght@400;700&family=Tinos:wght@400&display=swap">
<style>
  :root {
    --stage: #2e302f;
    --card-white: #ffffff;
    --green: #8fb06a;
    --gold: #a89466;
    --ink: #1f2320;
    --photo-sky: #5a6478;
    --photo-house: #7d8696;
    --photo-garden: #2f4230;
  }
  * { margin: 0; padding: 0; box-sizing: border-box; }
  html, body {
    width: 1200px; height: 1059px; overflow: hidden;
    background: var(--stage);
  }
  .stage { position: relative; width: 1200px; height: 1059px; }

  .card {
    position: absolute;
    border-radius: 18px;
    overflow: hidden;
  }

  /* Front */
  .card-front {
    left: 256px; top: 89px; width: 688px; height: 390px;
    background: var(--card-white);
    text-align: center;
  }
  .brand {
    position: absolute; left: 0; right: 0; top: 64px;
    font-family: "Tinos", serif; font-weight: 400; color: var(--green);
    line-height: 1;
  }
  .brand-main { display: block; font-size: 54px; }
  .brand-sub { display: block; font-size: 22px; margin-top: 12px; }

  .person-name {
    position: absolute; left: 0; right: 0; top: 214px;
    font-family: "Arimo", sans-serif; font-weight: 700;
    font-size: 26px; letter-spacing: 0.5px; color: var(--green);
  }
  .person-name .surname { color: var(--gold); }
  .person-title {
    position: absolute; left: 0; right: 0; top: 244px;
    font-family: "Arimo", sans-serif; font-size: 15.5px; color: var(--ink);
  }
  .divider {
    position: absolute; left: 329px; top: 273px;
    width: 30px; height: 1.5px; background: var(--green);
  }
  .contact {
    position: absolute; left: 0; right: 0;
    font-family: "Tinos", serif; font-size: 16.5px; color: var(--ink);
    display: flex; justify-content: center; align-items: center; gap: 6px;
  }
  .contact svg { width: 13px; height: 13px; fill: var(--green); flex: none; }
  .contact .sep { width: 12px; }
  .contact .accent { color: var(--gold); }
  .contact-address { top: 283px; }
  .contact-phone-web { top: 311px; }
  .contact-email { top: 339px; }

  /* Back */
  .card-back {
    left: 254px; top: 546px; width: 693px; height: 395px;
  }
  .building-photo {
    position: absolute; inset: 0;
    background: linear-gradient(180deg, var(--photo-sky) 0%, var(--photo-house) 35%, #6b6a5e 62%, var(--photo-garden) 85%, #3a4a36 100%);
  }
  .brand-back {
    position: absolute; left: 0; right: 0; top: 130px;
    text-align: center;
    font-family: "Tinos", serif; font-weight: 400; color: var(--green);
    line-height: 1;
  }
  .brand-back .brand-main { font-size: 60px; }
  .brand-back .brand-sub { font-size: 26px; margin-top: 12px; }
</style>
</head>
<body>
<div class="stage">

  <section class="card card-front">
    <div class="brand">
      <span class="brand-main">The Estate</span>
      <span class="brand-sub">at Brookhollow Golf Club</span>
    </div>

    <div class="person-name">MARLA <span class="surname">WHITCOMBE</span></div>
    <div class="person-title">President-Owner</div>
    <div class="divider"></div>

    <div class="contact contact-address">
      <svg viewBox="0 0 24 24"><path d="M12 1a8 8 0 0 0-8 8c0 6 8 14 8 14s8-8 8-14a8 8 0 0 0-8-8zm0 11a3 3 0 1 1 0-6 3 3 0 0 1 0 6z"/></svg>
      <span>2280 Hollins Lane Ridgeford, MD 21390</span>
    </div>

    <div class="contact contact-phone-web">
      <svg viewBox="0 0 24 24"><path d="M6.6 10.8a15 15 0 0 0 6.6 6.6l2.2-2.2a1 1 0 0 1 1-.25 11.4 11.4 0 0 0 3.6.6 1 1 0 0 1 1 1V20a1 1 0 0 1-1 1A17 17 0 0 1 3 4a1 1 0 0 1 1-1h3.5a1 1 0 0 1 1 1c0 1.25.2 2.45.6 3.6a1 1 0 0 1-.25 1z"/></svg>
      <span>(410) 555-0148</span>
      <span class="sep"></span>
      <svg viewBox="0 0 24 24"><path d="M12 2a10 10 0 1 0 0 20 10 10 0 0 0 0-20zm6.9 6h-3a15.6 15.6 0 0 0-1.4-3.6A8 8 0 0 1 18.9 8zM12 4c.8 1.2 1.5 2.5 1.9 4h-3.8c.4-1.5 1.1-2.8 1.9-4zM4.3 14a8 8 0 0 1 0-4h3.4a16 16 0 0 0 0 4zm.8 2h3a15.6 15.6 0 0 0 1.4 3.6A8 8 0 0 1 5.1 16zm3-8h-3a8 8 0 0 1 4.4-3.6C9 5.5 8.5 6.7 8.1 8zM12 20c-.8-1.2-1.5-2.5-1.9-4h3.8c-.4 1.5-1.1 2.8-1.9 4zm2.3-6H9.7a14.7 14.7 0 0 1 0-4h4.6a14.7 14.7 0 0 1 0 4zm.2 5.6c.6-1.1 1.100-2.3 1.4-3.6h3a8 8 0 0 1-4.4 3.6zm1.8-5.6a16 16 0 0 0 0-4h3.4a8 8 0 0 1 0 4z"/></svg>
      <span>www.<span class="accent">hollowmerevenue</span>.com</span>
    </div>

    <div class="contact contact-email">
      <svg viewBox="0 0 24 24"><path d="M2 5h20v14H2zm2 2v.5l8 5 8-5V7zm0 3v7h16v-7l-8 5z"/></svg>
      <span>mwhitcombe@hollowmerevenue.com</span>
    </div>
  </section>

  <section class="card card-back">
    <div class="building-photo" role="img" aria-label="Photograph of the white historic estate house at dusk with a curved columned porch, lit windows, green hedges and pink flowers along the front steps"></div>
    <div class="brand-back">
      <span class="brand-main">The Estate</span>
      <span class="brand-sub">at Brookhollow Golf Club</span>
    </div>
  </section>

</div>
</body>
</html>
```